Craft oriented film company needs a Business Card design

Hi all,
We're a 2-man band film company in New Zealand called Kestrel Pictures. We're good honest blokes, who are very passionate about the craft of film making. I've attached our current logo which has a bit of a crafty/artisan feel that we like. Feel free to use it - or throw the baby out with the bathwater and start again..... you never know, you might inspire a complete brand re-work.

In any case, the vibe we want to give out is that we are solid, dependable and no bullshit - but without compromising creative excellence and being in the now. We like the 'Brooklyn' artisan style of work.

Preferably single sided.

We need the standard stuff:
Name, job title, cellphone, email address and physical address (this can be smaller if you like - street, suburb, city & zip, country [if you want])

Check out our website to learn more about us: kestrelpictures.example

Target Market(s)

Brand marketers and advertising agency creatives looking for video production.

Industry/Entity Type

Baby

Requirements
Should not have
• Nothing flashy or too 'futuristic', we want it to feel grounded and real. A limited colour palette is preferred.
We don't want any film reels or cameras or anything obvious like that.

```html
<!DOCTYPE html>
<html lang="en">
<head>
<meta charset="utf-8">
<title>Kestrel Pictures — Business Card</title>
<link rel="stylesheet" href="https://fonts.googleapis.com/css2?family=Open+Sans:wght@400;600&display=swap">
<style>
  :root {
    --page-bg: #e4e1dc;
    --card-light: #f2f1ef;
    --card-mid: #dcdcda;
    --band-dark: #1c1c1c;
    --band-edge: #2b2b2b;
    --rim-teal: #7fa3a1;
    --accent-gold: #d8c2a2;
    --text-soft: #c9c0b3;
  }
  html, body {
    margin: 0;
    padding: 0;
    width: 1200px;
    height: 970px;
    overflow: hidden;
    background: var(--page-bg);
  }
  .business-card {
    position: absolute;
    left: 80px;
    top: 189px;
    width: 1040px;
    height: 592px;
    box-shadow: 0 18px 40px rgba(0,0,0,0.18);
  }
  .business-card svg { display: block; }
  .brand-name {
    font-family: "Open Sans", Arial, sans-serif;
    font-weight: 600;
    fill: var(--accent-gold);
    letter-spacing: 3px;
  }
  .person-name {
    font-family: "Open Sans", Arial, sans-serif;
    font-size: 31px;
    fill: var(--accent-gold);
    letter-spacing: 1px;
  }
  .person-role, .postal-address, .contact-line {
    font-family: "Open Sans", Arial, sans-serif;
    font-size: 21px;
    fill: var(--text-soft);
  }
  .contact-icon { fill: none; stroke: var(--accent-gold); stroke-width: 2; }
  .contact-icon-solid { fill: var(--accent-gold); }
</style>
</head>
<body>
  <div class="business-card">
    <svg width="1040" height="592" viewBox="0 0 1040 592" xmlns="http://www.w3.org/2000/svg">
      <defs>
        <linearGradient id="card-surface" x1="0" y1="0" x2="1" y2="1">
          <stop offset="0" stop-color="var(--card-light)"/>
          <stop offset="1" stop-color="var(--card-mid)"/>
        </linearGradient>
      </defs>

      <!-- card base -->
      <rect class="card-base" x="0" y="0" width="1040" height="592" fill="url(#card-surface)"/>

      <!-- teal rims around the band -->
      <path class="band-rim" d="M0 224 Q520 300 1040 224 L1040 566 Q520 500 0 566 Z" fill="var(--rim-teal)"/>

      <!-- dark centre band -->
      <path class="center-band" d="M0 234 Q520 310 1040 234 L1040 554 Q520 488 0 554 Z" fill="var(--band-dark)"/>

      <!-- brand seal -->
      <circle class="brand-seal" cx="520" cy="199" r="176" fill="var(--band-dark)" stroke="var(--rim-teal)" stroke-width="8"/>
      <text class="brand-name" x="520" y="192" font-size="46" text-anchor="middle">KESTREL</text>
      <text class="brand-name" x="520" y="248" font-size="46" text-anchor="middle">PICTURES</text>

      <!-- person -->
      <text class="person-name" x="64" y="359">ROWAN HALE</text>
      <text class="person-role" x="64" y="391">Director</text>

      <!-- address -->
      <text class="postal-address" x="64" y="439">418 Harbour Lane, Unit 3</text>
      <text class="postal-address" x="64" y="469">Ponsonby, Auckland 1011</text>

      <!-- contacts -->
      <text class="contact-line" x="938" y="398" text-anchor="end">+64-21-55-0147</text>
      <text class="contact-line" x="938" y="433" text-anchor="end">info@kestrelpictures.example</text>
      <text class="contact-line" x="938" y="468" text-anchor="end">kestrelpictures.example</text>

      <!-- phone icon -->
      <rect class="contact-icon" x="962" y="376" width="13" height="22" rx="2"/>
      <circle class="contact-icon-solid" cx="968.5" cy="394" r="1.4"/>

      <!-- mail icon -->
      <rect class="contact-icon-solid" x="958" y="415" width="22" height="15" rx="1"/>
      <path d="M958 416 L969 424 L980 416" fill="none" stroke="var(--band-dark)" stroke-width="1.6"/>

      <!-- globe icon -->
      <circle class="contact-icon" cx="969" cy="460" r="10"/>
      <ellipse class="contact-icon" cx="969" cy="460" rx="4.5" ry="10"/>
      <line class="contact-icon" x1="959" y1="460" x2="979" y2="460"/>
    </svg>
  </div>
</body>
</html>
```